Design a Business Card for a financial company

Looking for ideas for a new business card design.

What I am looking for:

1. Must be a "classic" business card design for a financial company. The design must be conservative.
2. Card stock will be white.
3. Design can incorporate horizontal or vertical logo. Logo should be red and text of logo should be dark blue. Text for the rest of the card should be matching dark blue.
4. Back of card should have logo as well as our website address: www.harborvest482.example
5. The back of the card can have a color to it but logo must be clearly visible.
6. You can visit our website to get styling cues of the colors of our company.
7. Assume that every card will have a full name, title, two line address, phone, fax and email address. See attached example of existing business card.
8. Font should be legible and not too small.
9. Final design should be provided in hi-resolution: .jpg, .AI, .eps, .png and .psd
10. Winner chosen will be given contact information of nine employees of company and must provide a proof for each business card.

Rules:

1. Please do not post public messages asking me to look at your submission - I will look at all of them.
2. Please post original ideas.
3. Ask questions and I will do my best to answer them quickly.

Good luck and thank you!

```html
<!DOCTYPE html>
<html lang="en">
<head>
<meta charset="utf-8">
<title>Harborvest Exchange Services – Business Card</title>
<link href="https://fonts.googleapis.com/css2?family=Lato:wght@400;700&display=swap" rel="stylesheet">
<style>
  :root {
    --navy: #1f3a66;
    --red: #9b1c2e;
    --card: #ffffff;
    --bg: #e6e7ea;
    --muted: #4a5a78;
  }
  * { box-sizing: border-box; margin: 0; padding: 0; }
  html, body { width: 1200px; height: 900px; overflow: hidden; }
  body {
    background: var(--bg);
    font-family: "Lato", Arial, sans-serif;
    color: var(--navy);
    position: relative;
  }
  .card {
    position: absolute;
    width: 630px;
    height: 360px;
    background: var(--card);
    box-shadow: 0 6px 18px rgba(0,0,0,0.12);
  }
  .card-back { left: 120px; top: 70px; }
  .card-front { left: 450px; top: 470px; }

  .brand { display: flex; align-items: center; gap: 14px; }
  .brand-dot { width: 58px; height: 58px; border-radius: 50%; background: var(--red); flex: none; }
  .brand-name { font-weight: 400; color: var(--navy); line-height: 1.1; }

  .card-back .brand { position: absolute; left: 120px; top: 120px; }
  .card-back .brand-name { font-size: 30px; }
  .back-web {
    position: absolute; left: 0; right: 0; top: 250px;
    text-align: center; font-size: 13px; letter-spacing: 3px; color: var(--muted);
  }

  .identity { position: absolute; left: 40px; top: 46px; padding-left: 14px; border-left: 4px solid var(--red); }
  .person-name { font-size: 24px; font-weight: 700; }
  .person-title { font-size: 15px; color: var(--muted); margin-top: 2px; }
  .address { position: absolute; left: 58px; top: 128px; font-size: 16px; line-height: 1.45; }
  .rule { position: absolute; left: 58px; top: 196px; width: 520px; height: 2px; background: var(--red); }
  .divider { position: absolute; left: 318px; top: 130px; width: 2px; height: 40px; background: var(--red); }

  .contact { position: absolute; display: flex; flex-direction: column; gap: 12px; font-size: 16px; }
  .contact-phone { left: 58px; top: 222px; }
  .contact-web { left: 348px; top: 70px; }
  .contact-row { display: flex; align-items: center; gap: 14px; }
  .contact-row svg { width: 18px; height: 18px; flex: none; }

  .card-front .brand { position: absolute; left: 360px; top: 250px; gap: 10px; }
  .card-front .brand-dot { width: 40px; height: 40px; }
  .card-front .brand-name { font-size: 19px; }
</style>
</head>
<body>
  <section class="card card-back">
    <div class="brand">
      <span class="brand-dot"></span>
      <span class="brand-name">Harborvest<br>Exchange Services, Inc.</span>
    </div>
    <p class="back-web">www.harborvest482.example</p>
  </section>

  <section class="card card-front">
    <div class="identity">
      <h1 class="person-name">Daniel R. Whitcombe, Esq</h1>
      <p class="person-title">Exchange Director</p>
    </div>
    <p class="address">412 Harbor Street, 8th Floor<br>Portland, ME 04101</p>
    <div class="divider"></div>
    <div class="rule"></div>

    <div class="contact contact-phone">
      <div class="contact-row">
        <svg viewBox="0 0 24 24" aria-hidden="true"><path fill="#9b1c2e" d="M6.6 10.8a15 15 0 0 0 6.6 6.6l2.2-2.2c.3-.3.7-.4 1-.2 1.1.4 2.3.6 3.6.6.6 0 1 .4 1 1V20c0 .6-.4 1-1 1A17 17 0 0 1 3 4c0-.6.4-1 1-1h3.5c.6 0 1 .4 1 1 0 1.3.2 2.5.6 3.6.1.3 0 .7-.2 1z"/></svg>
        <span>(877) 555-0148 x 210</span>
      </div>
      <div class="contact-row">
        <svg viewBox="0 0 24 24" aria-hidden="true"><rect x="6" y="3" width="12" height="6" fill="none" stroke="#9b1c2e" stroke-width="2"/><rect x="3" y="9" width="18" height="9" rx="1" fill="#9b1c2e"/><rect x="7" y="15" width="10" height="6" fill="#fff" stroke="#9b1c2e" stroke-width="2"/></svg>
        <span>(877) 555-0149</span>
      </div>
    </div>

    <div class="contact contact-web">
      <div class="contact-row">
        <svg viewBox="0 0 24 24" aria-hidden="true"><rect x="2" y="5" width="20" height="14" fill="#9b1c2e"/><path d="M2 5l10 8 10-8" fill="none" stroke="#fff" stroke-width="1.6"/></svg>
        <span>daniel@harborvest482.example</span>
      </div>
      <div class="contact-row">
        <svg viewBox="0 0 24 24" aria-hidden="true"><rect x="4" y="4" width="9" height="7" rx="2" fill="none" stroke="#9b1c2e" stroke-width="2"/><rect x="11" y="13" width="9" height="7" rx="2" fill="none" stroke="#9b1c2e" stroke-width="2"/></svg>
        <span>www.harborvest482.example</span>
      </div>
    </div>

    <div class="brand">
      <span class="brand-dot"></span>
      <span class="brand-name">Harborvest<br>Exchange Services, Inc.</span>
    </div>
  </section>
</body>
</html>
```